I am a pastry chef and just started my own business. I make all sorts of pastries: french macarons, petit fours, artisan chocolates, artisan bread, and they can be ordered on the website. I'm obsessed with Wonderland, so I'd like to have a logo & a background that incorporate that, something whimsical. I was thinking of a white rabbit wearing a chef toque - maybe he could have a monocle on. The logo could go on one side of the business card with "Tiny Baker of Moonbrook" on a banner of some sort at the bottom, and the contact & info could go on the other side. I'd like a really light color as the background, maybe a really light yellow.

Industry/Entity Type

Chef

Contact Information for Business Card

Tiny Baker of Moonbrook
Mira Delsan Corwick
tinybakerofmoonbrook.shopveltra.com
tinybakerofmoonbrook@mailquor.com
514-83-2071

```html
<!DOCTYPE html>
<html lang="en">
<head>
<meta charset="utf-8">
<title>Tiny Baker of Moonbrook — Business Card</title>
<link rel="stylesheet" href="https://fonts.googleapis.com/css2?family=Chewy&family=Kreon:wght@300;400&display=swap">
<style>
  :root {
    --page-bg: #6a8fae;
    --band-yellow: #f2ef9c;
    --panel-light: #b3c8da;
    --panel-mid: #9fb7cc;
    --panel-dark: #8aa5bd;
    --ink: #141012;
    --art-light: #ffffff;
    --art-shade: #d9dde2;
  }
  html, body {
    margin: 0;
    padding: 0;
    width: 1200px;
    height: 902px;
    overflow: hidden;
    background: var(--page-bg);
  }
  .card {
    position: absolute;
    left: 100px;
    top: 164px;
    width: 1000px;
    height: 573px;
    display: flex;
    flex-direction: column;
    box-shadow: 0 10px 30px rgba(20, 40, 60, 0.25);
  }
  .card__header {
    height: 151px;
    background: var(--band-yellow);
    display: flex;
    align-items: center;
    justify-content: center;
  }
  .card__title {
    margin: 0;
    font-family: "Kreon", serif;
    font-weight: 400;
    font-size: 52px;
    color: var(--ink);
  }
  .card__body {
    position: relative;
    height: 355px;
    background: radial-gradient(ellipse at 45% 40%, var(--panel-light) 0%, var(--panel-mid) 55%, var(--panel-dark) 100%);
  }
  .card__footer {
    height: 67px;
    background: var(--band-yellow);
  }
  .mascot-art {
    position: absolute;
    left: 47px;
    top: 26px;
    width: 332px;
    height: 298px;
    border-radius: 40px;
    background: radial-gradient(ellipse at 50% 55%, var(--art-light) 0%, var(--art-light) 45%, var(--art-shade) 75%, rgba(217, 221, 226, 0) 100%);
  }
  .contact {
    position: absolute;
    left: 456px;
    top: 52px;
  }
  .contact__name {
    margin: 0 0 52px;
    font-family: "Chewy", "Kreon", sans-serif;
    font-weight: 400;
    font-size: 36px;
    line-height: 44px;
    color: var(--ink);
  }
  .contact__list {
    list-style: none;
    margin: 0;
    padding: 0;
  }
  .contact__item {
    display: flex;
    align-items: center;
    height: 45px;
    font-family: "Kreon", serif;
    font-weight: 300;
    font-size: 26px;
    color: var(--ink);
    white-space: nowrap;
  }
  .contact__icon {
    width: 28px;
    height: 28px;
    margin-right: 16px;
    flex: none;
  }
</style>
</head>
<body>
  <main class="card">
    <header class="card__header">
      <h1 class="card__title">Tiny Baker of Moonbrook</h1>
    </header>

    <section class="card__body">
      <div class="mascot-art" role="img" aria-label="Illustration of a white rabbit wearing a chef's toque"></div>

      <div class="contact">
        <h2 class="contact__name">Mira Delsan Corwick</h2>
        <ul class="contact__list">
          <li class="contact__item">
            <svg class="contact__icon" viewBox="0 0 28 28" aria-hidden="true">
              <rect width="28" height="28" fill="var(--band-yellow)"/>
              <path d="M8 5 L11.5 5 L13 10 L10.8 11.8 C12 14.5 13.5 16 16.2 17.2 L18 15 L23 16.5 L23 20 C23 21.5 21.5 23 20 23 C12 22.5 5.5 16 5 8 C5 6.5 6.5 5 8 5 Z" fill="var(--ink)"/>
            </svg>
            514-83-2071
          </li>
          <li class="contact__item">
            <svg class="contact__icon" viewBox="0 0 28 28" aria-hidden="true">
              <rect width="28" height="28" fill="var(--band-yellow)"/>
              <rect x="4" y="7" width="20" height="14" fill="var(--ink)"/>
              <path d="M4.5 7.5 L14 15 L23.5 7.5" fill="none" stroke="var(--band-yellow)" stroke-width="1.6"/>
              <path d="M4.5 20.5 L11 13.5 M23.5 20.5 L17 13.5" fill="none" stroke="var(--band-yellow)" stroke-width="1.2"/>
            </svg>
            tinybakerofmoonbrook@mailquor.com
          </li>
          <li class="contact__item">
            <svg class="contact__icon" viewBox="0 0 28 28" aria-hidden="true">
              <rect width="28" height="28" fill="var(--band-yellow)"/>
              <circle cx="14" cy="14" r="10" fill="var(--ink)"/>
              <ellipse cx="14" cy="14" rx="4.5" ry="10" fill="none" stroke="var(--band-yellow)" stroke-width="1.3"/>
              <path d="M4 14 H24 M6 9 H22 M6 19 H22" stroke="var(--band-yellow)" stroke-width="1.3"/>
            </svg>
            tinybakerofmoonbrook.shopveltra.com
          </li>
        </ul>
      </div>
    </section>

    <footer class="card__footer"></footer>
  </main>
</body>
</html>
```